New Poster Design for Film Festival

Hi! We need a poster design for our student film festival and the Harlow Ridge University. We screen over 300 short films over a 3 days in May. Our committee wants a look feel similar to the image we attached below.

Target Market(s)

Students and general audience.

Industry/Entity Type

Festival

Colors
3377b5
85abd2
34b8a4
f68e4e

Requirements
Must have
• Otters Film Festival
17th Annual
May 2-3-4 2014
Ned Varrow Cinema
Free Admission
Department of Screen and Digital Narrative

Poster size 36" (high) x 24" (wide)
Harlow Ridge University
www.ottersfilmfest.example
Nice to have
• Bold lettering
Should not have
• Flamingos - hate them :)

```html
<!DOCTYPE html>
<html lang="en">
<head>
<meta charset="utf-8">
<title>Otters Film Festival – 17th Annual</title>
<link rel="stylesheet" href="https://fonts.googleapis.com/css2?family=Ubuntu:wght@500;700&display=swap">
<style>
  :root {
    --blue: #3377b5;
    --sky: #85abd2;
    --teal: #34b8a4;
    --orange: #f68e4e;
    --ink: #111111;
    --charcoal: #2b2b2b;
    --slate: #3f5a78;
    --white: #ffffff;
    --info-text: #3a3a3a;
  }
  html, body {
    margin: 0;
    padding: 0;
    width: 851px;
    height: 1200px;
    overflow: hidden;
    background: var(--white);
  }
  .poster {
    display: block;
    width: 851px;
    height: 1200px;
    font-family: "Ubuntu", sans-serif;
  }
  .outlined {
    font-weight: 700;
    stroke: var(--ink);
    paint-order: stroke fill;
    stroke-linejoin: round;
  }
  .title { font-size: 180px; stroke-width: 10px; }
  .title .word-one { fill: var(--white); }
  .title .word-two { fill: var(--orange); }
  .title .word-three { fill: var(--sky); }
  .edition { font-size: 72px; fill: var(--white); stroke-width: 7px; }
  .department { font-size: 28px; fill: var(--white); stroke-width: 5px; }
  .website { font-size: 46px; fill: var(--white); stroke-width: 6px; }
  .info-box { fill: var(--white); fill-opacity: 0.55; }
  .info-line {
    font-size: 30px;
    font-weight: 500;
    fill: var(--info-text);
  }
  .frame { fill: none; stroke: var(--charcoal); stroke-width: 2; }
</style>
</head>
<body>
<svg class="poster" viewBox="0 0 851 1200" xmlns="http://www.w3.org/2000/svg">
  <defs>
    <linearGradient id="dotsTone" x1="0" y1="0" x2="1" y2="1">
      <stop offset="0" stop-color="#85abd2"/>
      <stop offset="0.35" stop-color="#f68e4e"/>
      <stop offset="0.65" stop-color="#34b8a4"/>
      <stop offset="1" stop-color="#3377b5"/>
    </linearGradient>
    <radialGradient id="silhouetteTone" cx="0.5" cy="0.45" r="0.55">
      <stop offset="0" stop-color="#4a5f78"/>
      <stop offset="0.6" stop-color="#3b4652"/>
      <stop offset="1" stop-color="#2b2b2b" stop-opacity="0"/>
    </radialGradient>
  </defs>

  <g class="backdrop" role="img" aria-label="Pattern of overlapping blue, teal and orange dots over a dark state-shaped silhouette">
    <rect width="851" height="1200" fill="url(#dotsTone)" opacity="0.75"/>
    <rect x="150" y="100" width="640" height="780" rx="60" fill="url(#silhouetteTone)"/>
  </g>

  <text class="outlined title" transform="translate(142 1188) rotate(-90)" textLength="1166" lengthAdjust="spacingAndGlyphs"><tspan class="word-one">OTTERS</tspan> <tspan class="word-two">FILM</tspan> <tspan class="word-three">FESTIVAL</tspan></text>

  <text class="outlined edition" x="218" y="98" textLength="484" lengthAdjust="spacingAndGlyphs">17th ANNUAL</text>

  <text class="outlined department" transform="translate(823 903) rotate(-90)" textLength="880" lengthAdjust="spacingAndGlyphs">Department of Screen and Digital Narrative • Harlow Ridge University</text>

  <rect class="info-box" x="473" y="919" width="390" height="153" rx="14"/>
  <text class="info-line" x="815" y="972" text-anchor="end">May 2-3-4 2014</text>
  <text class="info-line" x="815" y="1007" text-anchor="end">Ned Varrow Cinema</text>
  <text class="info-line" x="815" y="1044" text-anchor="end">Free Admission</text>

  <text class="outlined website" x="169" y="1162" textLength="631" lengthAdjust="spacingAndGlyphs">www.ottersfilmfest.example</text>

  <rect class="frame" x="1" y="1" width="849" height="1198"/>
</svg>
</body>
</html>
```